Pediatric Dental Practice needs a postcard for direct mail advertising

We are looking for a creative and professional double-sided postcard design for a direct mail marketing campaign. Our goal is to attract new families to our pediatric dental practice by conveying a sense of warmth, modern care, and clinical excellence. The design should feel "boutique" and high-end yet remain fun and approachable for parents and children.

```html
<!DOCTYPE html>
<html lang="en">
<head>
<meta charset="utf-8">
<title>Birch Lane Pediatric Dentistry – Postcard</title>
<link href="https://fonts.googleapis.com/css2?family=Montserrat:wght@500;700;800&display=swap" rel="stylesheet">
<style>
  :root{
    --green:#2e9e5b;
    --green-mid:#4fb86f;
    --green-soft:#a6d9b0;
    --green-pale:#c9ebcf;
    --ink:#2f3a36;
    --white:#ffffff;
    --page:#ececec;
    --photo-warm:#e3dcb4;
    --photo-teal:#4f9fa8;
  }
  *{box-sizing:border-box;margin:0;padding:0}
  html,body{width:881px;height:1200px;overflow:hidden}
  body{background:var(--page);position:relative;font-family:"Montserrat",sans-serif}
  .card{position:absolute;left:77px;width:727px;height:520px;overflow:hidden;background:var(--white)}
  .card--front{top:63px}
  .card--back{top:618px}
  .card__inner{position:absolute;left:0;top:0;width:792px;height:566px;transform:scale(0.918);transform-origin:0 0}
  .card__art{position:absolute;inset:0;width:792px;height:566px}
  .brand{position:absolute;text-align:center;color:var(--ink);font-weight:500;font-size:27px;line-height:1.05;letter-spacing:.5px}
  .brand span{display:block;font-size:27px}
  .card--front .brand{left:296px;top:100px;width:200px}
  .card--back .brand{left:276px;top:100px;width:200px}
  .headline{position:absolute;color:var(--white);font-weight:800;line-height:1.2}
  .headline--front{right:52px;top:138px;text-align:right;font-size:41px;line-height:49px}
  .headline--front .headline__sub{display:block;font-size:24px;line-height:32px}
  .headline--back{left:40px;top:227px;font-size:33px;line-height:41px}
  .contact{position:absolute;list-style:none;color:var(--white);font-weight:500;font-size:15.5px;line-height:25px}
  .contact li{display:flex;align-items:flex-start;gap:8px}
  .contact svg{width:11px;height:11px;flex:none;margin-top:7px;fill:var(--white)}
  .contact--front{right:50px;top:389px;text-align:right}
  .contact--front li{justify-content:flex-end}
  .contact--front li svg{order:2}
  .contact--back{left:40px;top:389px}
  .contact .multi{line-height:19px;margin:3px 0}
  .stamp{position:absolute;left:655px;top:39px;width:92px;height:100px;border:1.5px solid var(--ink)}
  .address-line{position:absolute;left:537px;width:209px;height:0;border-top:1.5px solid var(--ink)}
</style>
</head>
<body>

<section class="card card--front">
  <div class="card__inner">
    <svg class="card__art" viewBox="0 0 792 566">
      <defs>
        <linearGradient id="roomTone" x1="0" y1="0" x2="1" y2="1">
          <stop offset="0" stop-color="var(--photo-warm)"/>
          <stop offset=".55" stop-color="#d6d6a8"/>
          <stop offset="1" stop-color="var(--photo-teal)"/>
        </linearGradient>
      </defs>
      <polygon points="670,0 792,120 792,566 222,566 410,262" fill="var(--green)"/>
      <polygon role="img" aria-label="Photo of a bright pediatric dental treatment room with a teal chair" points="0,0 165,0 314,176 330,176 509,368 336,566 0,566" fill="url(#roomTone)"/>
      <polygon points="0,0 95,0 170,90 0,210" fill="var(--green-soft)" opacity=".75"/>
      <line x1="0" y1="222" x2="344" y2="566" stroke="var(--white)" stroke-width="14"/>
      <line x1="0" y1="495" x2="322" y2="176" stroke="var(--white)" stroke-width="14"/>
    </svg>
    <div class="brand">Birch Lane<span>Pediatric Dentistry</span></div>
    <h1 class="headline headline--front">Creating<br>A Positive<br>Impact With<span class="headline__sub">Compassionate Care</span></h1>
    <ul class="contact contact--front">
      <li><svg viewBox="0 0 10 10"><path d="M2 0.5 3.6 2.6 2.7 3.6Q3.8 5.9 6.3 7.3L7.4 6.4 9.5 8 8.3 9.5Q1 7.5 0.5 1.7Z"/></svg>(555) 014-6000</li>
      <li><svg viewBox="0 0 10 10"><path d="M2.5 0.5H7.5V3H2.5ZM0.5 3.5H9.5V7.5H8V6H2V7.5H0.5ZM2.5 6.5H7.5V9.5H2.5Z"/></svg>(555) 014-6010</li>
      <li><svg viewBox="0 0 10 10"><path d="M0.5 2H9.5V8.5H0.5ZM1 2.5 5 5.5 9 2.5" stroke="var(--green)" stroke-width=".8"/></svg>hello@birchlanedental.com</li>
      <li class="multi"><svg viewBox="0 0 10 10"><path d="M5 0.3A3.3 3.3 0 0 1 8.3 3.6C8.3 6 5 9.7 5 9.7S1.7 6 1.7 3.6A3.3 3.3 0 0 1 5 .3ZM5 2.3A1.3 1.3 0 1 0 5 4.9 1.3 1.3 0 1 0 5 2.3Z"/></svg>48 Meadow Park Drive, Suite 210<br>Fairview, CT 06000</li>
      <li><svg viewBox="0 0 10 10"><circle cx="5" cy="5" r="4.5"/><path d="M0.5 5H9.5M5 .5V9.5" stroke="var(--green)" stroke-width=".8"/></svg>www.birchlanedental.com</li>
    </ul>
  </div>
</section>

<section class="card card--back">
  <div class="card__inner">
    <svg class="card__art" viewBox="0 0 792 566">
      <defs>
        <linearGradient id="backGreen" x1="0" y1="0" x2="1" y2="1">
          <stop offset="0" stop-color="var(--green-mid)"/>
          <stop offset="1" stop-color="#5fc07a"/>
        </linearGradient>
        <radialGradient id="backGlow" cx=".25" cy=".05" r=".7">
          <stop offset="0" stop-color="var(--green-pale)" stop-opacity=".9"/>
          <stop offset="1" stop-color="var(--green-pale)" stop-opacity="0"/>
        </radialGradient>
      </defs>
      <rect x="0" y="0" width="462" height="566" fill="url(#backGreen)"/>
      <path d="M0 0H300L340 120Q380 230 462 210V430Q300 380 240 300Q150 150 0 110Z" fill="url(#backGlow)"/>
      <polygon points="300,0 462,0 462,200 254,176" fill="var(--white)"/>
    </svg>
    <div class="brand">Birch Lane<span>Pediatric Dentistry</span></div>
    <h2 class="headline headline--back">Creating A Positive<br>Impact With<br>Compassionate Care</h2>
    <ul class="contact contact--back">
      <li><svg viewBox="0 0 10 10"><path d="M2 0.5 3.6 2.6 2.7 3.6Q3.8 5.9 6.3 7.3L7.4 6.4 9.5 8 8.3 9.5Q1 7.5 0.5 1.7Z"/></svg>(555) 014-6000</li>
      <li><svg viewBox="0 0 10 10"><path d="M2.5 0.5H7.5V3H2.5ZM0.5 3.5H9.5V7.5H8V6H2V7.5H0.5ZM2.5 6.5H7.5V9.5H2.5Z"/></svg>(555) 014-6010</li>
      <li><svg viewBox="0 0 10 10"><path d="M0.5 2H9.5V8.5H0.5ZM1 2.5 5 5.5 9 2.5" stroke="var(--green-mid)" stroke-width=".8"/></svg>hello@birchlanedental.com</li>
      <li class="multi"><svg viewBox="0 0 10 10"><path d="M5 0.3A3.3 3.3 0 0 1 8.3 3.6C8.3 6 5 9.7 5 9.7S1.7 6 1.7 3.6A3.3 3.3 0 0 1 5 .3ZM5 2.3A1.3 1.3 0 1 0 5 4.9 1.3 1.3 0 1 0 5 2.3Z"/></svg>48 Meadow Park Drive, Suite 210<br>Fairview, CT 06000</li>
      <li><svg viewBox="0 0 10 10"><circle cx="5" cy="5" r="4.5"/><path d="M0.5 5H9.5M5 .5V9.5" stroke="var(--green-mid)" stroke-width=".8"/></svg>www.birchlanedental.com</li>
    </ul>
    <div class="stamp"></div>
    <div class="address-line" style="top:376px"></div>
    <div class="address-line" style="top:419px"></div>
    <div class="address-line" style="top:463px"></div>
  </div>
</section>

</body>
</html>
```